plumbing & gas fitting business card design

We need a business card design for a plumbing & gas fitting company. The company covers commercial, domestic and maintenance work. We would like a modern design communicating efficiency and sophistication. preferred colours would include (red grey & black) or (green grey & black). Please DO NOT include any water droplets.

Industry/Entity Type

Business

Contact Information for Business Card

Vortig Plumbing & Gas, Commercial Domestic & Maintenance, licence no. 617394K, ABN 47215830962, Phone 0417382956, Email vortigplumbingandgas@corvanet.com

```html
<!DOCTYPE html>
<html lang="en">
<head>
<meta charset="utf-8">
<title>Vortig Plumbing &amp; Gas — Business Card</title>
<link rel="stylesheet" href="https://fonts.googleapis.com/css2?family=Comfortaa:wght@400;600;700&display=swap">
<style>
  :root {
    --page-bg: #ffffff;
    --card-bg: #1b1b1b;
    --pipe-red: #c8092b;
    --clamp-tone: #b00826;
    --ink: #141414;
  }
  html, body {
    margin: 0;
    padding: 0;
    width: 1200px;
    height: 1000px;
    overflow: hidden;
    background: var(--page-bg);
  }
  .business-card {
    display: block;
    width: 1200px;
    height: 1000px;
  }
  .card-face { fill: var(--card-bg); }
  .pipe-band { fill: var(--pipe-red); }
  .clamp-area { fill: var(--clamp-tone); }
  .card-text {
    font-family: "Comfortaa", sans-serif;
    fill: var(--ink);
  }
  .company-name { font-size: 31px; font-weight: 600; }
  .licence { font-size: 22px; font-weight: 600; }
  .services { font-size: 21px; font-weight: 600; }
  .email { font-size: 24px; font-weight: 600; }
  .abn { font-size: 21px; font-weight: 700; }
  .phone { font-size: 19px; font-weight: 700; }
</style>
</head>
<body>
<svg class="business-card" viewBox="0 0 1200 1000" xmlns="http://www.w3.org/2000/svg">
  <rect class="card-face" x="314" y="38" width="570" height="924"/>

  <!-- Company name -->
  <rect class="pipe-band" x="314" y="223" width="570" height="56"/>
  <rect class="clamp-area" x="331" y="206" width="56" height="91" rx="10" role="img" aria-label="Pipe clamp graphic"/>
  <text class="card-text company-name" x="405" y="263" textLength="465" lengthAdjust="spacingAndGlyphs">Vortig Plumbing &amp; Gas</text>

  <!-- Licence -->
  <rect class="pipe-band" x="314" y="304" width="570" height="56"/>
  <rect class="clamp-area" x="510" y="287" width="56" height="91" rx="10" role="img" aria-label="Pipe clamp graphic"/>
  <text class="card-text licence" x="626" y="341" textLength="244" lengthAdjust="spacingAndGlyphs">licence no. 617394K</text>

  <!-- Services -->
  <rect class="pipe-band" x="314" y="473" width="570" height="56"/>
  <rect class="clamp-area" x="331" y="455" width="56" height="91" rx="10" role="img" aria-label="Pipe clamp graphic"/>
  <text class="card-text services" x="395" y="509" textLength="475" lengthAdjust="spacingAndGlyphs">Commercial Domestic &amp; Maintenance</text>

  <!-- Email -->
  <rect class="pipe-band" x="314" y="554" width="570" height="56"/>
  <text class="card-text email" x="375" y="590" textLength="497" lengthAdjust="spacingAndGlyphs">vortigplumbingandgas@corvanet.com</text>

  <!-- ABN -->
  <rect class="pipe-band" x="314" y="638" width="570" height="56"/>
  <rect class="clamp-area" x="743" y="622" width="56" height="91" rx="10" role="img" aria-label="Pipe clamp graphic"/>
  <text class="card-text abn" x="387" y="674" textLength="230" lengthAdjust="spacingAndGlyphs">ABN 47215830962</text>

  <!-- Phone -->
  <rect class="pipe-band" x="640" y="811" width="244" height="56"/>
  <rect class="clamp-area" x="610" y="794" width="56" height="91" rx="10" role="img" aria-label="Pipe clamp graphic"/>
  <text class="card-text phone" x="730" y="846" textLength="144" lengthAdjust="spacingAndGlyphs">0417382956</text>
</svg>
</body>
</html>
```